Copperleaf Commons Apartments and Copperleaf Commons Apartments - Independent Senior Living
Corporate Stationary Design for Apartment Community - Real Estate
Corporate Stationary Design for Apartment Community
Professional
Martin Okafor
4715 Pebblecreek Lane Bryan, Texas 77615
manager@copperleaf-commons.example
mtorvek07 mtorvek07
Need to see letterhead and thank you cards. Not just business cards. Thanks!
Need corporate stationary design for the apartment community. Our apartment community is a mixture of senior housing and family housing so I would like the identical stationary design, but I need one to say "Independent Senior Living" underneath or by Copperleaf Commons Apartments. All in all there will be a total of two designs required.

```html
<!DOCTYPE html>
<html lang="en">
<head>
<meta charset="utf-8">
<title>Copperleaf Commons Apartments – Business Cards</title>
<link rel="stylesheet" href="https://fonts.googleapis.com/css2?family=Cinzel:wght@400;600&family=Cormorant+Garamond:wght@500&display=swap">
<style>
  :root {
    --backdrop: #5c5c5e;
    --maroon: #6b0f1f;
    --maroon-dark: #4e0815;
    --copper: #9a6a43;
    --paper: #ffffff;
    --ink: #3b1a1c;
    --faint-on-maroon: rgba(255, 255, 255, 0.12);
    --faint-on-paper: rgba(140, 110, 100, 0.18);
  }
  * { box-sizing: border-box; margin: 0; padding: 0; }
  html, body { width: 1200px; height: 908px; overflow: hidden; }
  body {
    background: var(--backdrop);
    font-family: "Cinzel", "Cormorant Garamond", serif;
    position: relative;
  }
  .card {
    position: absolute;
    top: 311px;
    width: 500px;
    height: 286px;
    border-radius: 14px;
    overflow: hidden;
  }
  .card-front { left: 60px; background: linear-gradient(160deg, var(--maroon) 0%, var(--maroon-dark) 100%); }
  .card-back { left: 640px; background: var(--paper); }

  .faint-ring { position: absolute; border-radius: 50%; }
  .card-front .faint-ring { width: 170px; height: 170px; right: 60px; top: 10px; border: 9px solid var(--faint-on-maroon); }
  .card-back .faint-ring { width: 150px; height: 150px; right: 18px; top: 18px; border: 8px solid var(--faint-on-paper); }

  .wordmark { position: absolute; color: #fff; }
  .card-front .wordmark { left: 40px; top: 192px; }
  .wordmark .name { font-size: 25px; font-weight: 400; letter-spacing: 0.5px; line-height: 1; white-space: nowrap; }
  .wordmark .sub { font-size: 10px; letter-spacing: 6px; margin-top: 5px; }
  .wordmark .tagline { font-size: 9px; letter-spacing: 2.4px; margin-top: 4px; white-space: nowrap; }

  .side-band { position: absolute; left: 36px; top: 0; bottom: 0; width: 30px; }
  .side-band .copper-part { height: 36%; background: var(--copper); }
  .side-band .maroon-part { height: 64%; background: var(--maroon); }

  .monogram-badge {
    position: absolute; left: 14px; top: 84px;
    width: 74px; height: 74px; border-radius: 50%;
    background: var(--paper); border: 3px solid var(--maroon);
    display: flex; align-items: center; justify-content: center; text-align: center;
    font-size: 9px; font-weight: 600; color: var(--maroon); line-height: 1.25;
  }

  .card-back .wordmark { left: 108px; top: 80px; color: var(--maroon); }
  .card-back .wordmark .name { font-size: 18px; }
  .card-back .wordmark .sub { font-size: 8px; letter-spacing: 5px; }
  .card-back .wordmark .tagline { font-size: 7.5px; letter-spacing: 1.8px; }

  .person-name {
    position: absolute; left: 108px; top: 146px;
    font-size: 15px; letter-spacing: 1px; color: var(--copper);
  }
  .contact {
    position: absolute; left: 108px; top: 182px;
    font-family: "Cormorant Garamond", serif; font-weight: 500;
    font-size: 13px; color: var(--ink); line-height: 1.35; list-style: none;
  }
  .contact li { display: flex; align-items: center; gap: 5px; white-space: nowrap; }
  .contact svg { width: 11px; height: 11px; flex: none; }
</style>
</head>
<body>
  <section class="card card-front" aria-label="Business card front">
    <div class="faint-ring"></div>
    <div class="wordmark">
      <div class="name">COPPERLEAF COMMONS</div>
      <div class="sub">APARTMENTS</div>
      <div class="tagline">INDEPENDENT SENIOR LIVING</div>
    </div>
  </section>

  <section class="card card-back" aria-label="Business card back">
    <div class="faint-ring"></div>
    <div class="side-band"><div class="copper-part"></div><div class="maroon-part"></div></div>
    <div class="monogram-badge">Copperleaf<br>Commons</div>
    <div class="wordmark">
      <div class="name">COPPERLEAF COMMONS</div>
      <div class="sub">APARTMENTS</div>
      <div class="tagline">INDEPENDENT SENIOR LIVING</div>
    </div>
    <div class="person-name">MARTIN OKAFOR</div>
    <ul class="contact">
      <li>4715 Pebblecreek Lane</li>
      <li>Bryan, Texas 77615</li>
      <li>
        <svg viewBox="0 0 12 12"><circle cx="6" cy="6" r="6" fill="#9a6a43"/><path d="M4 3.2c.4-.3.8-.2 1 .2l.4.8c.1.3 0 .5-.2.7l-.3.2c.3.7.8 1.2 1.5 1.5l.2-.3c.2-.2.4-.3.7-.2l.8.4c.4.2.5.6.2 1-.5.7-1.3.8-2 .4C5 7.2 4.2 6.4 3.6 5.3c-.4-.7-.3-1.5.4-2.1z" fill="#fff"/></svg>
        (979) 555-0148
      </li>
      <li>
        <svg viewBox="0 0 12 12"><circle cx="6" cy="6" r="6" fill="#9a6a43"/><rect x="3" y="3.8" width="6" height="4.4" fill="none" stroke="#fff" stroke-width=".9"/><path d="M3 3.8l3 2.4 3-2.4" fill="none" stroke="#fff" stroke-width=".9"/></svg>
        manager@copperleaf-commons.example
      </li>
    </ul>
  </section>
</body>
</html>
```